Design concept for PixelHarbor.com Support Page

We are about to launch a new support page for our www.pixelharbor.example service for photographers and visual artists. The service provides media management, cloud storage, promotional and secure distribution to our members.

The support page will include FAQs and video tutorials.

In particular we're looking for a header for this page that suggests the user is in the support area of our service - so perhaps an illustration that suggests support could look nice (perhaps repair man or doctor iconography). Something to give this area of our site a different look and something that looks both cool and friendly.

Currently the page looks distinctly sparse and undesigned (see attached screenshot) - something that could be remedied, we feel, by some subtle design enhancements that we can implement using CSS.

```html
<!DOCTYPE html>
<html lang="en">
<head>
<meta charset="utf-8">
<title>PixelHarbor Support</title>
<link rel="stylesheet" href="https://fonts.googleapis.com/css2?family=Questrial&family=Roboto:wght@300;400;500&display=swap">
<style>
:root{
  --red:#e8262a;
  --dark:#2e2e2f;
  --heading:#5d6670;
  --text:#7a7f84;
  --card:#f6f6f6;
  --line:#e5e5e5;
  --white:#ffffff;
  --icon:#e0e0e0;
}
*{box-sizing:border-box;margin:0;padding:0}
html,body{width:970px;height:1200px;overflow:hidden;background:var(--white)}
body{position:relative;font-family:'Roboto',sans-serif;color:var(--text)}
.site-header{position:absolute;left:0;top:0;width:970px;height:61px}
.brand{position:absolute;left:165px;top:16px;display:flex;align-items:center;gap:8px}
.brand-square{width:22px;height:22px;background:var(--heading)}
.brand-name{font-family:'Questrial',sans-serif;font-size:25px;color:var(--heading)}
.contact{position:absolute;right:163px;top:24px;display:flex;align-items:center;gap:10px;font-size:9.5px;color:var(--heading)}
.contact span{display:flex;align-items:center;gap:6px}
.header-band{position:absolute;left:0;top:61px;width:970px;height:15px;background:var(--dark)}

.support-art{position:absolute;left:590px;top:76px;width:232px;height:160px;
  background:radial-gradient(ellipse at 55% 40%,rgba(246,168,84,.30) 0,rgba(226,226,226,.45) 38%,rgba(240,240,240,.25) 60%,rgba(255,255,255,0) 75%);}

.help-title{position:absolute;left:163px;top:106px;font-family:'Questrial',sans-serif;font-size:24px;color:var(--heading)}
.help-lead{position:absolute;left:164px;top:143px;font-size:8.5px;color:#444}
.search{position:absolute;left:159px;top:170px;width:651px;height:38px;background:#ededed;border-radius:3px;padding:3px}
.search-field{width:100%;height:100%;background:#f7f7f7;display:flex;align-items:center;padding-left:11px;font-size:10px;color:#555}
.search-btn{position:absolute;right:3px;top:3px;width:41px;height:32px;background:var(--red);display:flex;align-items:center;justify-content:center}

.faq-card{position:absolute;width:302px;height:73px;background:var(--card);border:1px solid var(--line);border-radius:3px}
.faq-card .q-icon{position:absolute;left:13px;top:22px}
.faq-title{position:absolute;left:51px;top:14px;font-family:'Questrial',sans-serif;font-size:14.2px;font-weight:400;color:var(--red);white-space:nowrap;letter-spacing:.1px}
.faq-text{position:absolute;left:51px;top:36px;width:228px;font-size:8.3px;line-height:11px;font-weight:300;color:var(--text)}

.divider{position:absolute;left:157px;top:663px;width:652px;height:2px;background:#ececec}
.video-title{position:absolute;left:162px;top:695px;font-family:'Questrial',sans-serif;font-size:24px;color:var(--heading)}

.video-row{position:absolute;left:161px;width:650px;height:74px}
.video-tab{position:absolute;left:0;top:11px;width:40px;height:37px;background:var(--card);border:1px solid var(--line);border-right:none;border-radius:3px 0 0 3px;display:flex;align-items:center;justify-content:center}
.video-card{position:absolute;left:37px;top:0;width:613px;height:74px;background:var(--card);border:1px solid var(--line);border-radius:3px}
.video-name{position:absolute;left:20px;top:12px;font-weight:500;font-size:9.5px;color:var(--red)}
.video-text{position:absolute;left:19px;top:28px;width:232px;font-size:8.3px;line-height:10px;font-weight:300;color:var(--text)}
.video-table{position:absolute;left:268px;top:8px}
.video-table .head{display:flex;height:14px;font-size:8px;font-weight:500;color:#555}
.video-table .head .k{position:absolute;left:175px}
.video-table .head .l{position:absolute;left:270px}
.video-table .cells{position:absolute;top:14px;display:flex;height:31px;border:1px solid var(--line);background:#f9f9f9;font-size:8.3px;font-weight:300;color:var(--text)}
.cell{display:flex;align-items:center;height:100%;white-space:nowrap}
.cell-link{width:136px;padding-left:7px;gap:6px}
.cell-key{width:106px;justify-content:center;border-left:1px solid var(--line)}
.cell-len{width:83px;justify-content:center;border-left:1px solid var(--line)}

.site-footer{position:absolute;left:0;top:1122px;width:970px;height:78px;background:var(--dark);color:#f0f0f0;font-size:8.5px;text-align:center;padding-top:33px;line-height:11px}
</style>
</head>
<body>
<header class="site-header">
  <div class="brand"><div class="brand-square"></div><div class="brand-name">PixelHarbor</div></div>
  <div class="contact">
    <span><svg width="14" height="10" viewBox="0 0 14 10"><rect x="0.5" y="0.5" width="13" height="9" fill="none" stroke="#5d6670"/><path d="M0.5 0.5 7 6 13.5 0.5" fill="none" stroke="#5d6670"/></svg>help@pixelharbor.example</span>
    <span><svg width="16" height="16" viewBox="0 0 16 16"><circle cx="8" cy="8" r="7" fill="none" stroke="#5d6670"/><path d="M5.5 4.5c-.8.8 0 3 1.5 4.5s3.7 2.3 4.5 1.5l-1.2-1.3-1.2.6c-.8-.4-1.6-1.2-2-2l.6-1.2z" fill="#5d6670"/></svg>+00-0-555-0142</span>
  </div>
</header>
<div class="support-art" role="img" aria-label="Faint friendly support illustration behind the help heading"></div>
<div class="header-band"></div>

<main>
  <h1 class="help-title">We are happy to help you</h1>
  <p class="help-lead">If you can't find an answer to your PixelHarbor question, ask the search team!</p>
  <div class="search">
    <div class="search-field">Search your question.....</div>
    <div class="search-btn"><svg width="22" height="22" viewBox="0 0 22 22"><circle cx="9" cy="9" r="6.5" fill="none" stroke="#fff" stroke-width="2"/><path d="M14 14l6 6" stroke="#fff" stroke-width="2.6" stroke-linecap="round"/></svg></div>
  </div>

  <section class="faq">
    <article class="faq-card" style="left:159px;top:234px"><svg class="q-icon" width="26" height="26" viewBox="0 0 26 26"><circle cx="13" cy="13" r="13" fill="#e0e0e0"/><text x="13" y="19" text-anchor="middle" font-family="Roboto,sans-serif" font-weight="500" font-size="17" fill="#fff">?</text></svg><h3 class="faq-title">Proin vehicula justo hendreritehicula</h3><p class="faq-text">Nullam dignissim mi et sem aliquet cursus. Suspendisse mi nunc, feugiat a lacinia rhoncus, vulputate id ipsum. Aliquam</p></article>
    <article class="faq-card" style="left:507px;top:234px"><svg class="q-icon" width="26" height="26" viewBox="0 0 26 26"><circle cx="13" cy="13" r="13" fill="#e0e0e0"/><text x="13" y="19" text-anchor="middle" font-family="Roboto,sans-serif" font-weight="500" font-size="17" fill="#fff">?</text></svg><h3 class="faq-title">Proin vehicula justo hendreritehicula</h3><p class="faq-text">Nullam dignissim mi et sem aliquet cursus. Suspendisse mi nunc, feugiat a lacinia rhoncus, vulputate id ipsum. Aliquam</p></article>
    <article class="faq-card" style="left:159px;top:339px"><svg class="q-icon" width="26" height="26" viewBox="0 0 26 26"><circle cx="13" cy="13" r="13" fill="#e0e0e0"/><text x="13" y="19" text-anchor="middle" font-family="Roboto,sans-serif" font-weight="500" font-size="17" fill="#fff">?</text></svg><h3 class="faq-title">Proin vehicula justo hendreritehicula</h3><p class="faq-text">Nullam dignissim mi et sem aliquet cursus. Suspendisse mi nunc, feugiat a lacinia rhoncus, vulputate id ipsum. Aliquam</p></article>
    <article class="faq-card" style="left:507px;top:339px"><svg class="q-icon" width="26" height="26" viewBox="0 0 26 26"><circle cx="13" cy="13" r="13" fill="#e0e0e0"/><text x="13" y="19" text-anchor="middle" font-family="Roboto,sans-serif" font-weight="500" font-size="17" fill="#fff">?</text></svg><h3 class="faq-title">Proin vehicula justo hendreritehicula</h3><p class="faq-text">Nullam dignissim mi et sem aliquet cursus. Suspendisse mi nunc, feugiat a lacinia rhoncus, vulputate id ipsum. Aliquam</p></article>
    <article class="faq-card" style="left:159px;top:447px"><svg class="q-icon" width="26" height="26" viewBox="0 0 26 26"><circle cx="13" cy="13" r="13" fill="#e0e0e0"/><text x="13" y="19" text-anchor="middle" font-family="Roboto,sans-serif" font-weight="500" font-size="17" fill="#fff">?</text></svg><h3 class="faq-title">Proin vehicula justo hendreritehicula</h3><p class="faq-text">Nullam dignissim mi et sem aliquet cursus. Suspendisse mi nunc, feugiat a lacinia rhoncus, vulputate id ipsum. Aliquam</p></article>
    <article class="faq-card" style="left:507px;top:447px"><svg class="q-icon" width="26" height="26" viewBox="0 0 26 26"><circle cx="13" cy="13" r="13" fill="#e0e0e0"/><text x="13" y="19" text-anchor="middle" font-family="Roboto,sans-serif" font-weight="500" font-size="17" fill="#fff">?</text></svg><h3 class="faq-title">Proin vehicula justo hendreritehicula</h3><p class="faq-text">Nullam dignissim mi et sem aliquet cursus. Suspendisse mi nunc, feugiat a lacinia rhoncus, vulputate id ipsum. Aliquam</p></article>
    <article class="faq-card" style="left:159px;top:558px"><svg class="q-icon" width="26" height="26" viewBox="0 0 26 26"><circle cx="13" cy="13" r="13" fill="#e0e0e0"/><text x="13" y="19" text-anchor="middle" font-family="Roboto,sans-serif" font-weight="500" font-size="17" fill="#fff">?</text></svg><h3 class="faq-title">Proin vehicula justo hendreritehicula</h3><p class="faq-text">Nullam dignissim mi et sem aliquet cursus. Suspendisse mi nunc, feugiat a lacinia rhoncus, vulputate id ipsum. Aliquam</p></article>
    <article class="faq-card" style="left:507px;top:558px"><svg class="q-icon" width="26" height="26" viewBox="0 0 26 26"><circle cx="13" cy="13" r="13" fill="#e0e0e0"/><text x="13" y="19" text-anchor="middle" font-family="Roboto,sans-serif" font-weight="500" font-size="17" fill="#fff">?</text></svg><h3 class="faq-title">Proin vehicula justo hendreritehicula</h3><p class="faq-text">Nullam dignissim mi et sem aliquet cursus. Suspendisse mi nunc, feugiat a lacinia rhoncus, vulputate id ipsum. Aliquam</p></article>
  </section>

  <div class="divider"></div>
  <h2 class="video-title">Video Tutorials</h2>

  <section class="videos">
    <article class="video-row" style="top:739px">
      <div class="video-tab"><svg width="26" height="16" viewBox="0 0 26 16"><rect x="1" y="1.5" width="17" height="13" rx="1.5" fill="none" stroke="#e8262a" stroke-width="1.5"/><path d="M18 6l7-4v12l-7-4z" fill="none" stroke="#e8262a" stroke-width="1.5" stroke-linejoin="round"/></svg></div>
      <div class="video-card">
        <h3 class="video-name">Phasellus at enim ac tellus laoreet volutpat.</h3>
        <p class="video-text">Lorem ipsum dolor sit amet, consectetur adipiscing elit. In ac rhoncus ligula, eget pellentesque diam. Class aptedfdnt taciti sociosqu ad litora</p>
        <div class="video-table"><div class="head"><span class="k">Key#</span><span class="l">Length</span></div><div class="cells"><div class="cell cell-link"><svg width="12" height="12" viewBox="0 0 12 12"><circle cx="6" cy="6" r="6" fill="#e8262a"/><path d="M4.5 3.5v5l4-2.5z" fill="#fff"/></svg>Lorem ipsum dolor sit amet,</div><div class="cell cell-key">77725</div><div class="cell cell-len">04m:35s</div></div></div>
      </div>
    </article>
    <article class="video-row" style="top:832px">
      <div class="video-tab"><svg width="26" height="16" viewBox="0 0 26 16"><rect x="1" y="1.5" width="17" height="13" rx="1.5" fill="none" stroke="#e8262a" stroke-width="1.5"/><path d="M18 6l7-4v12l-7-4z" fill="none" stroke="#e8262a" stroke-width="1.5" stroke-linejoin="round"/></svg></div>
      <div class="video-card">
        <h3 class="video-name">Phasellus at enim ac tellus laoreet volutpat.</h3>
        <p class="video-text">Lorem ipsum dolor sit amet, consectetur adipiscing elit. In ac rhoncus ligula, eget pellentesque diam. Class aptedfdnt taciti sociosqu ad litora</p>
        <div class="video-table"><div class="head"><span class="k">Key#</span><span class="l">Length</span></div><div class="cells"><div class="cell cell-link"><svg width="12" height="12" viewBox="0 0 12 12"><circle cx="6" cy="6" r="6" fill="#e8262a"/><path d="M4.5 3.5v5l4-2.5z" fill="#fff"/></svg>Lorem ipsum dolor sit amet,</div><div class="cell cell-key">77725</div><div class="cell cell-len">04m:35s</div></div></div>
      </div>
    </article>
    <article class="video-row" style="top:925px">
      <div class="video-tab"><svg width="26" height="16" viewBox="0 0 26 16"><rect x="1" y="1.5" width="17" height="13" rx="1.5" fill="none" stroke="#e8262a" stroke-width="1.5"/><path d="M18 6l7-4v12l-7-4z" fill="none" stroke="#e8262a" stroke-width="1.5" stroke-linejoin="round"/></svg></div>
      <div class="video-card">
        <h3 class="video-name">Phasellus at enim ac tellus laoreet volutpat.</h3>
        <p class="video-text">Lorem ipsum dolor sit amet, consectetur adipiscing elit. In ac rhoncus ligula, eget pellentesque diam. Class aptedfdnt taciti sociosqu ad litora</p>
        <div class="video-table"><div class="head"><span class="k">Key#</span><span class="l">Length</span></div><div class="cells"><div class="cell cell-link"><svg width="12" height="12" viewBox="0 0 12 12"><circle cx="6" cy="6" r="6" fill="#e8262a"/><path d="M4.5 3.5v5l4-2.5z" fill="#fff"/></svg>Lorem ipsum dolor sit amet,</div><div class="cell cell-key">77725</div><div class="cell cell-len">04m:35s</div></div></div>
      </div>
    </article>
    <article class="video-row" style="top:1018px">
      <div class="video-tab"><svg width="26" height="16" viewBox="0 0 26 16"><rect x="1" y="1.5" width="17" height="13" rx="1.5" fill="none" stroke="#e8262a" stroke-width="1.5"/><path d="M18 6l7-4v12l-7-4z" fill="none" stroke="#e8262a" stroke-width="1.5" stroke-linejoin="round"/></svg></div>
      <div class="video-card">
        <h3 class="video-name">Phasellus at enim ac tellus laoreet volutpat.</h3>
        <p class="video-text">Lorem ipsum dolor sit amet, consectetur adipiscing elit. In ac rhoncus ligula, eget pellentesque diam. Class aptedfdnt taciti sociosqu ad litora</p>
        <div class="video-table"><div class="head"><span class="k">Key#</span><span class="l">Length</span></div><div class="cells"><div class="cell cell-link"><svg width="12" height="12" viewBox="0 0 12 12"><circle cx="6" cy="6" r="6" fill="#e8262a"/><path d="M4.5 3.5v5l4-2.5z" fill="#fff"/></svg>Lorem ipsum dolor sit amet,</div><div class="cell cell-key">77725</div><div class="cell cell-len">04m:35s</div></div></div>
      </div>
    </article>
  </section>
</main>

<footer class="site-footer">
  © Copyright 2014 Harborline Images Pte Ltd. All rights reserved.<br>
  Powered by PixelHarbor
</footer>
</body>
</html>
```